Stationary Design for Quince consultant and support company

We need new stationary designed for a London based support company that provide on-site and remote support services for Quince products. Our clients are both consumers and businesses.

We would like a letterhead, compliment slip, business card and possibly an e-mail signature designed.

Business card designs can be either 1 side or 2, depending on designs we receive we may choose a preference for 1 or 2 sides later on in the design stage.

Designs needs to be at least 300dpi and should be done using CMYK colours.

We want the design to be bold, easy to read, clean and professional.

We have attached our company logo in 2 colour variations (if you need any other source files then please ask).

Our logo colours are as follows:

Blue (85, 50, 0, 0) and Green (50, 0, 100, 0)

We use two different suppliers for out stationary so here are the size dimensions for both. Unfortunately they are ever so slightly different size wise so hopefully we can get something that accommodates both, we can provide dimensions if required for final versions.

Some fonts that have been used before with our company are Probert (for tagline on our company logo) and previously had Nauman used, however we are very much open to seeing what the designers come up with and the fonts mentioned are not a requirement.
Updates

Company details for designs (however the template should be editable for multiple staff) Vorbin Ltd. Registered Office: 62-74 Harlow Lane London N7 2QD 020 7915 3381 www.vorbin.example info@vorbin.example Company is Registered in England and Wales Company No. 07351649 Directors details (if you want to make the template using his details), rest of the details are as above Dan Moss Director dan@vorbin.example

Hi all, Thank you for your submissions so far. Could we please ask that you don't use the logo with the tagline from our website for the stationary designs and only the logos provided in the design brief. For the business cards we are looking at normal rectangular business cards to be used and we can provide a template guide for size if needed, please just ask. Regards Vorbin Team

Target Market(s)

Our target market are consumers (of all ages) and small/medium businesses.

Industry/Entity Type

Business

Font styles to use
Serif
Sans Serif

Requirements
Must have
• At least business card, letterhead and compliment slip submitted (we need all 3 designed this time round)
Should not have
• Business cards should not have the writing "registered office" (letterheads and compliment slips can along the bottom edge)

```html
<!DOCTYPE html>
<html lang="en">
<head>
<meta charset="utf-8">
<title>Vorbin Stationery Set</title>
<link rel="stylesheet" href="https://fonts.googleapis.com/css2?family=Montserrat:wght@400;600;700&display=swap">
<style>
  :root {
    --blue: #2f74b5;
    --blue-deep: #24598c;
    --green: #8cc04b;
    --ink: #2b2b2b;
    --muted: #7a7a7a;
    --paper: #fbfbfb;
    --backdrop: #e4e4e4;
  }
  * { box-sizing: border-box; margin: 0; padding: 0; }
  html, body { width: 1200px; height: 1000px; overflow: hidden; }
  body {
    position: relative;
    background: var(--backdrop);
    font-family: "Montserrat", Arial, sans-serif;
    color: var(--ink);
  }
  .sheet {
    position: absolute;
    background: var(--paper);
    box-shadow: 0 2px 6px rgba(0,0,0,.12);
    overflow: hidden;
  }
  .brand {
    font-weight: 700;
    color: var(--ink);
    letter-spacing: .04em;
    display: inline-flex;
    align-items: center;
    gap: 5px;
  }
  .brand .brand-dot { background: var(--green); display: inline-block; }

  /* Letterhead */
  .letterhead { left: 60px; top: 60px; width: 300px; height: 424px; padding: 36px 30px; }
  .letterhead .brand { font-size: 17px; }
  .letterhead .brand-dot { width: 9px; height: 9px; }
  .letter-body { margin-top: 26px; font-size: 6px; line-height: 1.6; color: var(--muted); }
  .letter-body .salutation { color: var(--ink); font-size: 6.5px; margin-bottom: 8px; }
  .letter-body p { margin-bottom: 10px; }
  .letter-close { text-align: right; font-size: 6.5px; color: var(--ink); margin-top: 12px; }
  .signature { width: 70px; height: 16px; margin: 10px 0 0 auto; background: linear-gradient(90deg, #d9d9d9, #c9c9c9); border-radius: 3px; }
  .letter-footer { position: absolute; left: 30px; bottom: 22px; font-size: 4.5px; line-height: 1.5; color: var(--muted); }
  .letter-footer .brand { font-size: 8px; margin-bottom: 3px; }
  .letter-footer .brand-dot { width: 5px; height: 5px; }

  /* Envelopes */
  .envelope { width: 320px; height: 160px; }
  .envelope-open { left: 400px; top: 80px; }
  .envelope-open .flap { position: absolute; left: 0; top: 0; width: 100%; height: 70px; background: var(--blue); }
  .envelope-open .flap-lining { position: absolute; left: 0; top: 0; width: 100%; height: 26px; background: var(--blue-deep); }
  .envelope-closed { left: 760px; top: 280px; }
  .envelope-closed .flap { position: absolute; left: 0; top: 0; width: 100%; height: 42px; background: var(--blue); border-radius: 0 0 6px 6px; }
  .return-address { position: absolute; right: 22px; bottom: 22px; font-size: 4.5px; line-height: 1.5; color: var(--muted); }
  .return-address .brand { font-size: 7px; margin-bottom: 2px; }
  .return-address .brand-dot { width: 4px; height: 4px; }

  .envelope-front { left: 760px; top: 80px; }
  .envelope-front .band-blue { position: absolute; left: 0; top: 0; width: 70px; height: 100%; background: var(--blue); }
  .envelope-front .band-green { position: absolute; left: 80px; top: 0; width: 26px; height: 100%; background: var(--green); }
  .envelope-front .brand { position: absolute; left: 150px; top: 64px; font-size: 16px; }
  .envelope-front .brand-dot { width: 8px; height: 8px; }

  /* Business card */
  .business-card { left: 445px; top: 290px; width: 170px; height: 100px; }
  .business-card .band-blue { position: absolute; left: 0; top: 0; width: 40px; height: 100%; background: var(--blue); }
  .business-card .band-green { position: absolute; left: 45px; top: 0; width: 12px; height: 100%; background: var(--green); }
  .card-details { position: absolute; left: 72px; top: 22px; font-size: 4.5px; line-height: 1.5; color: var(--muted); }
  .card-details .brand { font-size: 10px; margin-bottom: 4px; }
  .card-details .brand-dot { width: 5px; height: 5px; }
  .card-details .person { font-size: 6px; font-weight: 600; color: var(--ink); }

  /* Folder cover */
  .folder-cover { left: 60px; top: 520px; width: 300px; height: 420px; }
  .folder-cover .band-blue { position: absolute; left: 0; top: 0; width: 170px; height: 100%; background: var(--blue); }
  .folder-cover .band-green-top { position: absolute; right: 0; top: 0; width: 90px; height: 130px; background: var(--green); }
  .folder-cover .band-green-bottom { position: absolute; right: 0; bottom: 0; width: 90px; height: 140px; background: var(--green); }
  .folder-cover .brand { position: absolute; left: 186px; top: 198px; font-size: 16px; }
  .folder-cover .brand-dot { width: 8px; height: 8px; }

  /* Folder inside spread */
  .folder-inside { left: 400px; top: 480px; width: 680px; height: 460px; }
  .folder-inside .spine { position: absolute; left: 339px; top: 0; width: 2px; height: 100%; background: #e6e6e6; }
  .pocket { position: absolute; bottom: 0; width: 320px; height: 150px; border-radius: 18px 18px 0 0; }
  .pocket-left { left: 10px; background: var(--blue); }
  .pocket-right { right: 10px; background: var(--green); }
  .folder-inside .brand { position: absolute; right: 40px; top: 250px; font-size: 16px; }
  .folder-inside .brand-dot { width: 8px; height: 8px; }
</style>
</head>
<body>

  <section class="sheet letterhead">
    <div class="brand"><span class="brand-dot"></span>Vorbin</div>
    <div class="letter-body">
      <p class="salutation">Dear Client,</p>
      <p>We are pleased to confirm our on-site and remote support plan for your team. Our engineers will visit at the agreed time and keep you updated throughout.</p>
      <p>Please find the service summary enclosed with this letter. If anything is unclear, our help desk is open every weekday.</p>
      <p>Thank you for choosing us. We look forward to working with you again.</p>
    </div>
    <p class="letter-close">Best regards</p>
    <div class="signature" role="img" aria-label="Handwritten signature of Paul Grant"></div>
    <div class="letter-footer">
      <div class="brand"><span class="brand-dot"></span>Vorbin</div>
      <div>Vorbin Ltd.</div>
      <div>62-74 Harlow Lane London N7 2QD</div>
      <div>020 7915 3381</div>
      <div>www.vorbin.example</div>
      <div>info@vorbin.example</div>
    </div>
  </section>

  <section class="sheet envelope envelope-open">
    <div class="flap"></div>
    <div class="flap-lining"></div>
    <div class="return-address">
      <div class="brand"><span class="brand-dot"></span>Vorbin</div>
      <div>62-74 Harlow Lane London N7 2QD</div>
      <div>020 7915 3381</div>
      <div>www.vorbin.example</div>
    </div>
  </section>

  <section class="sheet envelope envelope-front">
    <div class="band-blue"></div>
    <div class="band-green"></div>
    <div class="brand"><span class="brand-dot"></span>Vorbin</div>
  </section>

  <section class="sheet business-card">
    <div class="band-blue"></div>
    <div class="band-green"></div>
    <div class="card-details">
      <div class="brand"><span class="brand-dot"></span>Vorbin</div>
      <div class="person">Dan Moss</div>
      <div>Director</div>
      <div>020 7915 3381</div>
      <div>dan@vorbin.example</div>
    </div>
  </section>

  <section class="sheet envelope envelope-closed">
    <div class="flap"></div>
    <div class="return-address">
      <div class="brand"><span class="brand-dot"></span>Vorbin</div>
      <div>62-74 Harlow Lane London N7 2QD</div>
      <div>020 7915 3381</div>
      <div>www.vorbin.example</div>
    </div>
  </section>

  <section class="sheet folder-cover">
    <div class="band-blue"></div>
    <div class="band-green-top"></div>
    <div class="band-green-bottom"></div>
    <div class="brand"><span class="brand-dot"></span>Vorbin</div>
  </section>

  <section class="sheet folder-inside">
    <div class="spine"></div>
    <div class="brand"><span class="brand-dot"></span>Vorbin</div>
    <div class="pocket pocket-left"></div>
    <div class="pocket pocket-right"></div>
  </section>

</body>
</html>
```